Law Firm in Texas in need of new letterhead

Law Firm in Fort Worth, TX, USA named "Pell & Whitcombe, Attorneys-At-Law, LLP." This is a general practice law firm that mostly does Family Law and Criminal Defense work.

We are looking for a new letterhead that has a "classical" appeal, with modern elements.

Any color combination is fine, but please note that we do fax many documents, so the design must be clearly legible in Black and White.

We would like our letterhead to project a sense of professionalism, integrity, and ability.

Target Market(s)

Letterhead will be for correspondence generally with other attorneys and clients.

Industry/Entity Type

Law Firm

Logo Text

Pell & Whitcombe, Attorneys-At-Law, LLP.

Logo styles of interest
Pictorial/Combination Logo
Wordmark Logo
Lettermark Logo
Requirements
Nice to have
• Although not necessary, a "Texas Star" that is incorporated into the design would be a nice touch.
Should not have
• Colors that do not convert to B&W easily

```html
<!DOCTYPE html>
<html lang="en">
<head>
<meta charset="utf-8">
<title>Pell &amp; Whitcombe Letterhead</title>
<link rel="stylesheet" href="https://fonts.googleapis.com/css2?family=Carlito:wght@400;700&display=swap">
<style>
:root{
  --backdrop:#e9e6e2;
  --paper:#ffffff;
  --band:#231f20;
  --band-text:#ffffff;
  --ink:#231f20;
  --watermark:#e4e4e4;
}
*{margin:0;padding:0;box-sizing:border-box}
html,body{width:1200px;height:1000px;overflow:hidden}
body{background:var(--backdrop);font-family:"Carlito",Calibri,Arial,sans-serif;color:var(--ink);position:relative}
.sheet{position:absolute;top:107px;width:534px;height:753px;background:var(--paper);box-shadow:0 2px 8px rgba(0,0,0,.25);overflow:hidden}
.sheet--blank{left:40px}
.sheet--letter{left:601px}
.masthead{position:absolute;left:0;top:0;width:100%;height:50px;background:var(--band);color:var(--band-text)}
.firm-name{position:absolute;left:13px;top:19px;font-size:15px;font-weight:700;white-space:nowrap;letter-spacing:-.1px}
.address,.contacts{position:absolute;top:16px;font-size:10.5px;line-height:13px}
.address{left:307px}
.contacts{left:438px}
.contact-line{display:flex;align-items:center;gap:2px}
.contact-line svg{width:10px;height:10px}
.watermark{position:absolute;left:119px;top:228px;width:300px;height:300px;border-radius:50%;
  background:radial-gradient(circle,var(--watermark) 0%,#f0f0f0 45%,rgba(240,240,240,.6) 70%,#ececec 71%,#ececec 74%,transparent 75%)}
.letter{position:absolute;left:38px;top:138px;width:460px;font-size:9.6px;line-height:12.9px}
.letter p{margin:0}
.letter .gap{height:12.9px}
.letter .salutation{margin-bottom:12.9px}
.letter .signature{margin-top:12.9px;padding-left:2px}
.footer{position:absolute;left:0;bottom:0;width:100%;height:46px;border-top:2px solid var(--band);padding:5px 3px 0;font-size:8.4px;line-height:10.6px;white-space:nowrap}
.footer strong{font-weight:700}
</style>
</head>
<body>

<section class="sheet sheet--blank">
  <header class="masthead">
    <div class="firm-name">Pell &amp; Whitcombe, Attorneys-at-Law, LLP</div>
    <div class="address">2140 W. Magnolia Ave.<br>Fort Worth, TX 76110</div>
    <div class="contacts">
      <div class="contact-line"><svg viewBox="0 0 10 10"><path d="M2.2 1 3.8 2.8 3 4c.6 1.3 1.6 2.3 3 3l1.2-.8L9 7.8 8 9C4.5 8.8 1.2 5.5 1 2z" fill="none" stroke="#fff" stroke-width=".8"/></svg>(817) 555-0142</div>
      <div class="contact-line"><svg viewBox="0 0 10 10"><rect x="2.5" y="1" width="5" height="3" fill="none" stroke="#fff" stroke-width=".8"/><rect x="1" y="4" width="8" height="3.5" fill="none" stroke="#fff" stroke-width=".8"/><rect x="2.5" y="6.5" width="5" height="2.5" fill="#fff"/></svg>(817) 555-0187</div>
    </div>
  </header>
  <div class="watermark" role="img" aria-label="Faint Texas star in a circle watermark"></div>
  <footer class="footer">
    Partners:<br>
    <strong>Daniel Pell</strong>, Managing Partner (Licensed in State of Texas, United States District Court (Northern District of Texas), United States Supreme Court)<br>
    <strong>Laura Jean Whitcombe</strong> (Licensed in the State of Texas)
  </footer>
</section>

<section class="sheet sheet--letter">
  <header class="masthead">
    <div class="firm-name">Pell &amp; Whitcombe, Attorneys-at-Law, LLP</div>
    <div class="address">2140 W. Magnolia Ave.<br>Fort Worth, TX 76110</div>
    <div class="contacts">
      <div class="contact-line"><svg viewBox="0 0 10 10"><path d="M2.2 1 3.8 2.8 3 4c.6 1.3 1.6 2.3 3 3l1.2-.8L9 7.8 8 9C4.5 8.8 1.2 5.5 1 2z" fill="none" stroke="#fff" stroke-width=".8"/></svg>(817) 555-0142</div>
      <div class="contact-line"><svg viewBox="0 0 10 10"><rect x="2.5" y="1" width="5" height="3" fill="none" stroke="#fff" stroke-width=".8"/><rect x="1" y="4" width="8" height="3.5" fill="none" stroke="#fff" stroke-width=".8"/><rect x="2.5" y="6.5" width="5" height="2.5" fill="#fff"/></svg>(817) 555-0187</div>
    </div>
  </header>
  <div class="watermark" role="img" aria-label="Faint Texas star in a circle watermark"></div>
  <article class="letter">
    <p class="salutation">Dear Addressee Name:</p>
    <p>Andipsum dipsum nostis nulpute magnissis niatie te molor adignis sequips uscipisit, sit vel ipsuscing ent lut lan ulla feugait augueraesto odolore doluptatio cons dolor sismodo luptatuero do od dolore magnim dolor auguero eu facilis ea core estrud eugiat velis ad tat dio odolor augue magna corting eugait enim venibh et, quatumsan hendre tincinisi tisisl dolute moloreet atem velesequat alit aliquat, vel dolore faciduis dolore dignis dolorper il eugiamconsed deliquamcon henis alis atum duis at.</p>
    <p>Bore del ute faccum vercill aorper sent alit, venis autet, quipsustio eugue vero dolore velendre euis nos nonse dolessim illa feum dolor sumsan ectet lortincin vulputat amet, qui esto conulput acil in eugait vel essequam zzriusto diam, velit wissit autat.</p>
    <p>Obore dolor incip ea conummy nulput vel ullan henisim am in ute erciliqui ex ent et, quis augiat, commod tis enis num delit laor acing elis dolorer se eugue feu facinci liquis aut lut nulluptat er sum zzrit vulla consequis accum incidunt iusci blaortio odoloreet pratum veliquatie modit, quat. Ut nummodo exercilisl iriliqu ipsusto dolesequat. Ut wisl in ute consequam ad diam vulputpat lan hent vel doloreet utat ver si.</p>
    <div class="gap"></div>
    <p>Vullaorem iusci blamcon seniamcommy nit iureetum dolore con ea faccum iureet prat. In utat acidunt nullum venismolum ing exer iusci bla augue magna consequi tem veliquis nostion utpat.</p>
    <p>Nibh euipis esed ero doluptat. Ibh ex exeros exero dolesed dunt pratissi euis nismodipsum eu feuguerit ipisl incilla faccum am init praese tat velis augue corem iriliqu amconsequat. Magnim ipit in ea acincil esto et wisl esenim volenit lorem del ut aut la commy nibh eui tiniam iure mod tem vel ipisit, quis nonse-qui blan exerosto odolorem il irit num vel dolore et irit aute te dolestrud tin hent utet ut praestrud ea faccum venim venim il er iustion sequipsum quat.</p>
    <div class="gap"></div>
    <p>Do ea acilisis dolore min ercing endre consequat. Ero consequis ad euguerat, siscidunt laor sum iuscipis nullaoreet, velent ilit amconul laorperit lore diatum dui bla facipit irit alis ad dolorpe rostrud tem esse-quat praesequam, coreet ip er sim dit, velisim inciliquam, quis adigna feugue dolore et irillaor.</p>
    <p>Adiam zzrit,</p>
    <p class="signature">Veliquatin Veraessi</p>
  </article>
  <footer class="footer">
    Partners:<br>
    <strong>Daniel Pell</strong>, Managing Partner (Licensed in State of Texas, United States District Court (Northern District of Texas), United States Supreme Court)<br>
    <strong>Laura Jean Whitcombe</strong> (Licensed in the State of Texas)
  </footer>
</section>

</body>
</html>
```